Grivo like IOS/Android app for Okinawa Island - TavuScout

TavuScout is the name of the app
The closest thing that I can relate this app to is a region specific Grivo app. The app is for the island of Okinawa and is geared towards English speaking travelers. The style of app that I prefer is a look and feel similar to that of the new Lodgemere app, color should also be similar if not the same as the lodgemere app.

The app needs to have the following screens

LOGIN SCREEN
1. App login page with a login for chatterly button or create an account option. Personally I would like an image in the background with a real beachy feel, but don't do this if it messes with your design.

2. Depending on the choice of login there will need to be a second login screen to create the account. Lodgemere does this nicely.

PRIMARY HOME
primary page similar to the primary layout when you get into the lodgemere app.
This page is kind of like the home page of the app and should include the following items:
search field
upcoming events
popular things to do
featured restaurants
Featured Places to stay
area guides
Moving here
(this will allow the person to select, housing agencies, auto dealers, schools etc) These are essentially just quick searches.
Each selection should be listed so that the user can swipe to the left or right in order to view more listings under the categories listed above. It will not be the full list but rather a sample.

SIDEBAR POPOUT MENU
Popout sidebar that contains the following selections
Places to Eat
Things to do
Attractions
Beaches
Shop
Farmers Markets
Places to Stay
Schools & DayCare
Housing
Auto
Events
Account settings
Add a business

LIST VIEW
4. List view page for whatever category the user selected. This will show all the listings for the specific category: The top should also have the featured listings for that category

INDIVIDUAL LISTING
5. Listing page
This will include photos, description, hours, map(this can be a button to view the map or the map), Reviews with a leave a review option

AREA GUIDES
6. Area Guides. This is where the user will be able to select a specific area and learn about it. It should include an area where there can be a description, photos with a hero photo image, a map, popular local attractions or things to do, best restaurants in the area, places to stay etc.

PROFILE PAGE
7. Profile page for the user where they can make any updates they need to

Every page but the listing page should include the search bar. When the user clicks in it they should be able to see a drop down of quick select searches or run a regular search.

Logo
I have attached a logo that was made that needs a redesign. The map marker contains the logo for Okinawa within it so it does need to be similar.

If you have any questions or need clarification please send me a message. I will respond promptly.
Thank you,

```html
<!DOCTYPE html>
<html lang="en">
<head>
<meta charset="utf-8">
<title>TavuScout – Sidebar Menu</title>
<link href="https://fonts.googleapis.com/css2?family=Lato:wght@400;700&display=swap" rel="stylesheet">
<style>
  :root {
    --brand: #ea5d6b;
    --brand-shade: rgba(0,0,0,0.07);
    --ink: #3a3a3a;
    --icon: #505050;
    --muted-white: rgba(255,255,255,0.75);
    --drawer-bg: #ffffff;
    --active-bg: #f3f3f3;
    --scrim: #555555;
    --scrim-status: #4a2f33;
    --scrim-card: #6b6b6b;
    --scrim-photo: #3e3b3c;
    --scrim-accent: #8e3a43;
  }
  html, body {
    margin: 0;
    padding: 0;
    width: 1200px;
    height: 2933px;
    overflow: hidden;
    background: #ffffff;
    font-family: "Lato", sans-serif;
  }
  .screen {
    position: absolute;
    left: 0;
    top: 0;
    width: 360px;
    height: 880px;
    transform: scale(3.33333);
    transform-origin: 0 0;
    overflow: hidden;
    background: var(--scrim);
  }
  .home-behind { position: absolute; inset: 0; }
  .home-status {
    position: absolute;
    left: 0; top: 0;
    width: 360px; height: 24px;
    background: var(--scrim-status);
  }
  .more-link {
    position: absolute;
    left: 303px;
    font-size: 14px;
    font-weight: 700;
    color: var(--scrim-accent);
  }
  .card {
    position: absolute;
    width: 120px;
    height: 160px;
    border-radius: 6px;
    background: var(--scrim-card);
    overflow: hidden;
  }
  .card-photo {
    height: 112px;
    background: linear-gradient(180deg, #4a4143, var(--scrim-photo));
  }
  .drawer {
    position: absolute;
    left: 0; top: 0;
    width: 300px; height: 880px;
    background: var(--drawer-bg);
    z-index: 2;
  }
  .drawer-header {
    position: relative;
    height: 208px;
    background: var(--brand);
  }
  .drawer-header::before {
    content: "";
    position: absolute;
    left: 0; top: 0;
    width: 300px; height: 24px;
    background: var(--brand-shade);
  }
  .status-icons {
    position: absolute;
    right: 8px; top: 4px;
    display: flex;
    align-items: center;
    gap: 5px;
    color: #fff;
    font-size: 13px;
    line-height: 16px;
    z-index: 3;
  }
  .avatar {
    position: absolute;
    left: 16px; top: 48px;
    width: 76px; height: 76px;
    border-radius: 50%;
    border: 2px solid #fff;
    background: linear-gradient(160deg, #d9d9d4, #7fa8a0);
  }
  .user-name {
    position: absolute;
    left: 17px; top: 150px;
    margin: 0;
    font-size: 16px;
    line-height: 20px;
    font-weight: 700;
    color: #fff;
  }
  .view-profile {
    position: absolute;
    left: 17px; top: 174px;
    font-size: 13px;
    line-height: 16px;
    color: var(--muted-white);
  }
  .profile-chevron { position: absolute; left: 264px; top: 164px; }
  .menu { list-style: none; margin: 0; padding: 0; }
  .menu-item {
    display: flex;
    align-items: center;
    height: 56px;
    font-size: 14px;
    color: var(--ink);
  }
  .menu-item svg { margin-left: 17px; width: 24px; height: 24px; fill: var(--icon); flex: none; }
  .menu-item span { margin-left: 32px; }
  .menu-item.is-active { background: var(--active-bg); color: var(--brand); }
  .menu-item.is-active svg { fill: var(--brand); }
</style>
</head>
<body>
<div class="screen">

  <div class="home-behind" aria-hidden="true">
    <div class="home-status"></div>
    <div class="more-link" style="top:235px">MORE</div>
    <div class="card" style="left:196px;top:280px"><div class="card-photo" role="img" aria-label="Listing photo"></div></div>
    <div class="card" style="left:332px;top:280px"><div class="card-photo" role="img" aria-label="Listing photo"></div></div>
    <div class="more-link" style="top:515px">MORE</div>
    <div class="card" style="left:196px;top:560px"><div class="card-photo" role="img" aria-label="Listing photo"></div></div>
    <div class="card" style="left:332px;top:560px"><div class="card-photo" role="img" aria-label="Listing photo"></div></div>
    <div class="more-link" style="top:795px">MORE</div>
    <div class="card" style="left:196px;top:840px"><div class="card-photo" role="img" aria-label="Listing photo"></div></div>
    <div class="card" style="left:332px;top:840px"><div class="card-photo" role="img" aria-label="Listing photo"></div></div>
  </div>

  <div class="status-icons">
    <svg width="16" height="14" viewBox="0 0 16 14"><path d="M8 13 0 3a13 13 0 0 1 16 0z" fill="#fff"/></svg>
    <svg width="14" height="14" viewBox="0 0 14 14"><path d="M14 0v14H0z" fill="#fff"/></svg>
    <svg width="8" height="14" viewBox="0 0 8 14"><rect x="0" y="2" width="8" height="12" rx="1" fill="#fff"/><rect x="2" y="0" width="4" height="2" fill="#fff"/></svg>
    <span>12:30</span>
  </div>

  <nav class="drawer">
    <header class="drawer-header">
      <div class="avatar" role="img" aria-label="User profile photo"></div>
      <h2 class="user-name">Owen Talbridge</h2>
      <div class="view-profile">View profile</div>
      <svg class="profile-chevron" width="16" height="16" viewBox="0 0 16 16"><path d="M5 3l5 5-5 5" stroke="#fff" stroke-width="2" fill="none"/></svg>
    </header>

    <ul class="menu">
      <li class="menu-item"><svg viewBox="0 0 24 24"><path d="M4 2h1.5v6H7V2h1.5v6H10V2h1v7a3 3 0 0 1-2.5 3V22h-2V12A3 3 0 0 1 4 9zM16 2c2.5 0 4 2.5 4 6v6h-2v8h-2z"/></svg><span>Places to Eat</span></li>
      <li class="menu-item"><svg viewBox="0 0 24 24"><path d="M12 2a10 10 0 1 1 0 20 10 10 0 0 1 0-20zm0 2a8 8 0 1 0 0 16 8 8 0 0 0 0-16zM8.5 8a1.5 1.5 0 1 1 0 3 1.5 1.5 0 0 1 0-3zm7 0a1.5 1.5 0 1 1 0 3 1.5 1.5 0 0 1 0-3zM7 14h10a5 5 0 0 1-10 0z"/></svg><span>Things to do</span></li>
      <li class="menu-item"><svg viewBox="0 0 24 24"><path d="M14 6l-4 5.5 3 4-1.6 1.2L6 10l-6 8h24z" transform="translate(0 -1)"/></svg><span>Attractions</span></li>
      <li class="menu-item"><svg viewBox="0 0 24 24"><path d="M13 4a9 9 0 0 1 8 8l-3-1-2 2-2-2-1 1 7 7-1.4 1.4-7-7-1 1 2 2-2 2 1 3a9 9 0 0 1-8-8z"/></svg><span>Beaches</span></li>
      <li class="menu-item is-active"><svg viewBox="0 0 24 24"><path d="M3 4h18v2H3zm-1 4h20v3h-1v9h-2v-6h-5v6H3v-9H2zm3 6v4h5v-4z"/></svg><span>Shop</span></li>
      <li class="menu-item"><svg viewBox="0 0 24 24"><path d="M12 8a4 4 0 1 1 0 8 4 4 0 0 1 0-8zm0-6 2 4h-4zm0 20-2-4h4zM2 12l4-2v4zm20 0-4 2v-4zM5 5l4 1.5L6.5 9zm14 14-4-1.5 2.5-2.5zM19 5l-1.5 4L15 6.5zM5 19l1.5-4L9 17.5z"/></svg><span>Farmers market</span></li>
      <li class="menu-item"><svg viewBox="0 0 24 24"><path d="M2 7h2v7h7V9h9a2 2 0 0 1 2 2v7h-2v-2H4v2H2zm5 3a2 2 0 1 1 0 3 2 2 0 0 1 0-3z"/></svg><span>Places to Stay</span></li>
      <li class="menu-item"><svg viewBox="0 0 24 24"><path d="M12 3 1 9l11 6 9-4.9V17h2V9zM5 13.2v4L12 21l7-3.8v-4L12 17z"/></svg><span>Schools and Daycare</span></li>
      <li class="menu-item"><svg viewBox="0 0 24 24"><path d="M10 20v-6h4v6h5v-8h3L12 3 2 12h3v8z"/></svg><span>Housing</span></li>
      <li class="menu-item"><svg viewBox="0 0 24 24"><path d="M18.9 6A1.5 1.5 0 0 0 17.5 5h-11A1.5 1.5 0 0 0 5.1 6L3 12v8a1 1 0 0 0 1 1h1a1 1 0 0 0 1-1v-1h12v1a1 1 0 0 0 1 1h1a1 1 0 0 0 1-1v-8zM6.5 16a1.5 1.5 0 1 1 0-3 1.5 1.5 0 0 1 0 3zm11 0a1.5 1.5 0 1 1 0-3 1.5 1.5 0 0 1 0 3zM5 11l1.5-4.5h11L19 11z"/></svg><span>Auto</span></li>
      <li class="menu-item"><svg viewBox="0 0 24 24"><path d="M17 12h-5v5h5zM16 1v2H8V1H6v2H5a2 2 0 0 0-2 2v14a2 2 0 0 0 2 2h14a2 2 0 0 0 2-2V5a2 2 0 0 0-2-2h-1V1zm3 18H5V8h14z"/></svg><span>Events</span></li>
      <li class="menu-item"><svg viewBox="0 0 24 24"><path d="M10 4h4a2 2 0 0 1 2 2v1h4a2 2 0 0 1 2 2v4h-9v-1h-2v1H2V9a2 2 0 0 1 2-2h4V6a2 2 0 0 1 2-2zm0 3h4V6h-4zM2 14h9v1h2v-1h9v5a2 2 0 0 1-2 2H4a2 2 0 0 1-2-2z"/></svg><span>Add a business</span></li>
    </ul>
  </nav>

</div>
</body>
</html>
```